Veltrona Services

Double sided business cards with color on front and black and white on back. I have basic ideas and graphics, but am looking for someone to take them to the next level

```html
<!DOCTYPE html>
<html lang="en">
<head>
<meta charset="utf-8">
<title>Veltrona Services – Business Card</title>
<link rel="stylesheet" href="https://fonts.googleapis.com/css2?family=Poppins:wght@500;700;800&family=Quicksand:wght@600&family=Lato:wght@400&display=swap">
<style>
  :root {
    --backdrop: #b8b8b8;
    --brand-purple: #5c51a8;
    --paper: #ffffff;
    --ink: #1b1b1b;
    --black: #000000;
  }
  * { margin: 0; padding: 0; box-sizing: border-box; }
  html, body { width: 1200px; height: 801px; overflow: hidden; }
  body { background: var(--backdrop); position: relative; font-family: "Lato", sans-serif; }

  .card {
    position: absolute; top: 274px; width: 443px; height: 263px;
    overflow: hidden; box-shadow: 2px 2px 2px rgba(0,0,0,0.85);
  }
  .card--front { left: 153px; background: var(--paper); }
  .card--back { left: 625px; background: var(--brand-purple); }

  .band { position: absolute; top: 0; height: 100%; }
  .card--front .band { left: 278px; width: 135px; background: var(--brand-purple); }
  .card--back .band--white { left: 281px; width: 136px; background: var(--paper); }

  .disc {
    position: absolute; left: 268px; top: 54px; width: 154px; height: 154px;
    border-radius: 50%; background: var(--paper);
    display: flex; align-items: center; justify-content: center;
  }
  .network-art {
    width: 126px; height: 126px; border-radius: 50%;
    background: radial-gradient(circle, #f4eef8 0%, #e2d4ec 55%, #c9a8dc 80%, #f0c46a 92%, #d9534f 100%);
  }

  .company {
    position: absolute; left: 23px; top: 29px;
    font-family: "Poppins", sans-serif; font-weight: 700; font-size: 20.5px;
    color: var(--brand-purple); letter-spacing: 0.2px;
  }
  .person { position: absolute; left: 24px; top: 76px; }
  .person__name {
    font-family: "Quicksand", sans-serif; font-weight: 600; font-size: 17px;
    color: var(--brand-purple); line-height: 1.2;
  }
  .person__role { font-size: 12px; color: var(--ink); line-height: 1.3; }

  .contacts { position: absolute; left: 23px; top: 170px; list-style: none; }
  .contacts li { display: flex; align-items: center; gap: 6px; height: 18.5px; color: var(--ink); font-size: 12px; }
  .contacts li:first-child { font-size: 14px; height: 21px; }
  .contacts svg { width: 14px; height: 14px; flex: none; }

  .slogan {
    position: absolute; left: 31px; top: 95px; color: var(--paper);
    font-family: "Poppins", sans-serif; font-weight: 800; text-transform: uppercase;
    text-shadow: 1.5px 1.5px 0 var(--black); line-height: 1;
  }
  .slogan__lead { display: block; font-size: 35px; letter-spacing: 0.3px; }
  .slogan__rest { display: block; font-size: 17.4px; line-height: 23px; margin-top: 1px; letter-spacing: -0.2px; }

  .card--back .disc { left: 268px; }
  .mark { display: flex; align-items: center; gap: 5px; }
  .mark__dot { width: 12px; height: 12px; border-radius: 50%; background: var(--black); }
  .mark__name { font-family: "Poppins", sans-serif; font-weight: 800; font-size: 17px; color: var(--black); }
</style>
</head>
<body>
  <section class="card card--front" aria-label="Front of business card">
    <div class="band"></div>
    <div class="disc">
      <div class="network-art" role="img" aria-label="Colourful circular network illustration of connected lines and dots"></div>
    </div>
    <h1 class="company">VELTRONA SERVICES</h1>
    <div class="person">
      <p class="person__name">Marcus Ellery</p>
      <p class="person__role">Managing Director</p>
    </div>
    <ul class="contacts">
      <li>
        <svg viewBox="0 0 14 14" aria-hidden="true"><rect x="0.7" y="0.7" width="12.6" height="12.6" rx="2" fill="none" stroke="#5c51a8" stroke-width="1.2"/><path d="M4 3.5l1.6-.4.9 2-1 .8a5 5 0 0 0 2.6 2.6l.8-1 2 .9-.4 1.6c-3.4.4-6.9-3.1-6.5-6.5z" fill="#5c51a8"/></svg>
        555-014-2837
      </li>
      <li>
        <svg viewBox="0 0 14 14" aria-hidden="true"><rect x="0" y="2.5" width="14" height="9" fill="#5c51a8"/><path d="M0 2.5l7 5 7-5M0 11.5l5-4.5M14 11.5l-5-4.5" fill="none" stroke="#fff" stroke-width="1"/></svg>
        hello@veltrona.com
      </li>
      <li>
        <svg viewBox="0 0 14 14" aria-hidden="true"><g fill="none" stroke="#5c51a8" stroke-width="1.1"><circle cx="7" cy="7" r="6.3"/><ellipse cx="7" cy="7" rx="2.8" ry="6.3"/><path d="M0.7 7h12.6M1.7 3.8h10.6M1.7 10.2h10.6"/></g></svg>
        www.veltrona.com
      </li>
    </ul>
  </section>

  <section class="card card--back" aria-label="Back of business card">
    <div class="band band--white"></div>
    <p class="slogan">
      <span class="slogan__lead">A Curated</span>
      <span class="slogan__rest">Experience all that is</span>
      <span class="slogan__rest">promised is clarity</span>
    </p>
    <div class="disc">
      <div class="mark">
        <span class="mark__dot"></span>
        <span class="mark__name">VELTRONA</span>
      </div>
    </div>
  </section>
</body>
</html>
```